Tr construction holdings pty ltd

2 sided card black and red with white
Very professional and elegant

Target Market(s)

Construction and Development

Industry/Entity Type

Construction and development

Contact Information for Business Card

One side black, one side red/or white business logo in top corner, email: morgan@trbuildworks.example

Requirements
Should not have
• Blue

```html
<!DOCTYPE html>
<html lang="en">
<head>
<meta charset="utf-8">
<title>TR Construction – Business Card</title>
<link rel="stylesheet" href="https://fonts.googleapis.com/css2?family=Montserrat:wght@700&family=Arimo:wght@400&display=swap">
<style>
  :root {
    --backdrop: #2a2a2a;
    --card-black: #050505;
    --brand-red: #e63a1f;
    --paper-white: #ffffff;
  }
  * { box-sizing: border-box; margin: 0; padding: 0; }
  html, body {
    width: 1200px;
    height: 900px;
    overflow: hidden;
    background: var(--backdrop);
  }
  .canvas {
    width: 1200px;
    height: 900px;
    display: flex;
    flex-direction: column;
    align-items: center;
    justify-content: center;
    gap: 24px;
  }
  .card {
    position: relative;
    width: 700px;
    height: 400px;
    box-shadow: 0 12px 30px rgba(0,0,0,0.55);
    overflow: hidden;
  }
  .card--front { background: var(--card-black); }
  .card--back { background: var(--brand-red); }
  .edge-band {
    position: absolute;
    left: 0; right: 0; bottom: 0;
    height: 10px;
    background: var(--brand-red);
  }
  .wordmark {
    position: absolute;
    left: 0; right: 0;
    text-align: center;
    font-family: "Montserrat", sans-serif;
    font-weight: 700;
    font-size: 40px;
    line-height: 1;
    letter-spacing: 0.08em;
    color: var(--paper-white);
    text-transform: uppercase;
  }
  .card--front .wordmark { top: 165px; }
  .card--back .wordmark { top: 75px; }

  .contact {
    position: absolute;
    left: 60px; right: 60px;
    top: 225px;
    display: flex;
    flex-direction: column;
    align-items: center;
    gap: 10px;
    color: var(--paper-white);
  }
  .contact-icon {
    width: 22px; height: 22px;
    border-radius: 50%;
    background: var(--paper-white);
    display: flex; align-items: center; justify-content: center;
  }
  .contact-row {
    width: 100%;
    display: flex;
    align-items: center;
    gap: 14px;
  }
  .contact-rule {
    flex: 1;
    height: 2px;
    background: var(--paper-white);
  }
  .contact-email {
    font-family: "Arimo", sans-serif;
    font-size: 19px;
    letter-spacing: 0.01em;
    white-space: nowrap;
  }
  .contact-dots { display: flex; gap: 18px; }
  .contact-dots span {
    width: 6px; height: 6px;
    border-radius: 50%;
    background: var(--paper-white);
  }
</style>
</head>
<body>
  <main class="canvas">
    <section class="card card--front" aria-label="Card front">
      <div class="wordmark">TR Construction</div>
      <div class="edge-band"></div>
    </section>

    <section class="card card--back" aria-label="Card back">
      <div class="wordmark">TR Construction</div>
      <div class="contact">
        <div class="contact-icon">
          <svg width="12" height="9" viewBox="0 0 12 9" aria-hidden="true">
            <rect x="0.5" y="0.5" width="11" height="8" fill="none" stroke="#e63a1f" stroke-width="1"/>
            <path d="M0.5 0.5 L6 5 L11.5 0.5" fill="none" stroke="#e63a1f" stroke-width="1"/>
          </svg>
        </div>
        <div class="contact-row">
          <span class="contact-rule"></span>
          <span class="contact-email">morgan@trbuildworks.example</span>
          <span class="contact-rule"></span>
        </div>
        <div class="contact-dots"><span></span><span></span><span></span></div>
      </div>
    </section>
  </main>
</body>
</html>
```